stationary design
Brightway Journeys
Project: stationary design
stationary design - Travel
Creative Brief
Professional
Ibrahim Naseer
Managing Director
H. Fehimaage, Kanbaafaru Higun, Male' Maldives.
naseer@brightwayjourney.example
www.brightwayjourney.example

```html
<!DOCTYPE html>
<html lang="en">
<head>
<meta charset="utf-8">
<title>Brightway Journeys – Business Card</title>
<link href="https://fonts.googleapis.com/css2?family=Cinzel:wght@400;600;700&family=Lato:wght@400;700&display=swap" rel="stylesheet">
<style>
  :root {
    --navy: #1f3c88;
    --navy-deep: #182f6e;
    --gold: #e3a12a;
    --paper: #ffffff;
    --ink: #3a3f4a;
    --stage: #e9eaee;
    --rule: #c9ccd4;
  }
  * { box-sizing: border-box; margin: 0; padding: 0; }
  html, body {
    width: 1200px; height: 988px; overflow: hidden;
    background: var(--stage);
  }
  .canvas {
    width: 1200px; height: 988px;
    display: flex; flex-direction: column; align-items: center; justify-content: center;
    gap: 40px;
  }
  .card {
    width: 760px; height: 434px;
    position: relative; overflow: hidden;
    box-shadow: 0 6px 18px rgba(20, 30, 60, 0.18);
  }

  /* Back side */
  .card--back {
    background: var(--navy);
    color: var(--paper);
    display: flex; flex-direction: column; align-items: center; justify-content: center;
  }
  .back-name {
    font-family: "Cinzel", serif; font-weight: 600;
    font-size: 40px; letter-spacing: 3px; color: var(--paper);
    display: flex; align-items: center; gap: 18px;
  }
  .back-name .mark { width: 26px; height: 26px; background: var(--paper); }
  .back-url {
    position: absolute; left: 0; right: 0; bottom: 58px; text-align: center;
    font-family: "Cinzel", serif; font-size: 15px; letter-spacing: 5px;
  }

  /* Front side */
  .card--front { background: var(--paper); }
  .brand {
    position: absolute; top: 50px; left: 0; right: 0;
    display: flex; align-items: center; justify-content: center; gap: 16px;
    font-family: "Cinzel", serif; font-weight: 600;
    font-size: 38px; letter-spacing: 2px; color: var(--navy);
  }
  .brand .mark { width: 30px; height: 30px; border: 3px solid var(--gold); }
  .details {
    position: absolute; top: 150px; left: 70px; right: 70px;
    display: flex; justify-content: center;
  }
  .person {
    text-align: right; padding-right: 26px; width: 50%;
    border-right: 1px solid var(--rule);
  }
  .person-name {
    font-family: "Cinzel", serif; font-weight: 700;
    font-size: 19px; letter-spacing: 1.5px; color: var(--navy);
  }
  .person-title {
    font-family: "Cinzel", serif; font-size: 14px; color: var(--ink);
    margin-top: 4px; margin-bottom: 14px;
  }
  .person-address {
    font-family: "Cinzel", serif; font-size: 13px; line-height: 1.5; color: var(--ink);
  }
  .contacts { list-style: none; padding-left: 22px; width: 50%; }
  .contacts li {
    display: flex; align-items: center; gap: 10px;
    font-family: "Lato", sans-serif; font-size: 13.5px; color: var(--ink);
    height: 24px;
  }
  .contacts svg { width: 17px; height: 17px; flex: none; }
  .gold-rule {
    position: absolute; left: 0; right: 0; bottom: 66px; height: 4px; background: var(--gold);
  }
  .front-band {
    position: absolute; left: 0; right: 0; bottom: 0; height: 58px;
    background: var(--navy-deep);
    display: flex; align-items: center; justify-content: center;
    font-family: "Cinzel", serif; font-size: 15px; letter-spacing: 5px; color: var(--paper);
  }
</style>
</head>
<body>
<main class="canvas">

  <section class="card card--back" aria-label="Card back">
    <div class="back-name"><span class="mark"></span>Brightway Journeys</div>
    <div class="back-url">www.brightwayjourney.example</div>
  </section>

  <section class="card card--front" aria-label="Card front">
    <div class="brand"><span class="mark"></span>Brightway Journeys</div>

    <div class="details">
      <div class="person">
        <div class="person-name">Ibrahim Naseer</div>
        <div class="person-title">Managing Director</div>
        <div class="person-address">H. Fehimaage, Kanbaafaru Higun,<br>Male' Maldives.</div>
      </div>
      <ul class="contacts">
        <li>
          <svg viewBox="0 0 20 20" aria-hidden="true"><circle cx="10" cy="10" r="10" fill="var(--navy)"/><path d="M6.5 5.5l2 0 1 2.5-1.2 1a6 6 0 0 0 2.7 2.7l1-1.2 2.5 1v2a1 1 0 0 1-1 1A8.5 8.5 0 0 1 5.5 6.5a1 1 0 0 1 1-1z" fill="#fff"/></svg>
          +9600004120
        </li>
        <li>
          <svg viewBox="0 0 20 20" aria-hidden="true"><circle cx="10" cy="10" r="10" fill="var(--navy)"/><rect x="7" y="4.5" width="6" height="11" rx="1" fill="#fff"/><rect x="8" y="6" width="4" height="6.5" fill="var(--navy)"/></svg>
          +9600007385
        </li>
        <li>
          <svg viewBox="0 0 20 20" aria-hidden="true"><circle cx="10" cy="10" r="10" fill="var(--navy)"/><rect x="5" y="8" width="10" height="6" rx="1" fill="#fff"/><rect x="7" y="5" width="6" height="3.5" fill="#fff"/></svg>
          +9600004121
        </li>
        <li>
          <svg viewBox="0 0 20 20" aria-hidden="true"><circle cx="10" cy="10" r="10" fill="var(--navy)"/><rect x="5" y="6.5" width="10" height="7" fill="#fff"/><path d="M5 6.5l5 4 5-4" stroke="var(--navy)" stroke-width="1" fill="none"/></svg>
          naseer@brightwayjourney.example
        </li>
      </ul>
    </div>

    <div class="gold-rule"></div>
    <div class="front-band">www.brightwayjourney.example</div>
  </section>

</main>
</body>
</html>
```